Honey Jar Label
Dellacourt Brothers Pine Cove Honey
Honey Jar Label - Food
Creative Brief
Dellacourt Brothers Pine Cove Wild and Raw Honey is produced by thousands of hardworking honeybees in the remote coastal area of Big Sur, California. The bees are surrounded by Federal Woodland Trust land, so no pesticides come in contact with the bees or this honey. The honey is collected by Jasper (10), Ottis (7) and Rowan Dellacourt (5) with help from their Dad.
Food
Target audience is high end organic food consumer
Need Label that is 2.25 x 6.75 inches, mounted horizontally on four sided clear glass bottle.
Concepts
label design for a popcorn brand

```html
<!DOCTYPE html>
<html lang="en">
<head>
<meta charset="utf-8">
<title>Dellacourt Brothers Pine Cove Honey – Jar Label</title>
<link rel="stylesheet" href="https://fonts.googleapis.com/css2?family=Arimo:ital,wght@0,400;0,700;1,400&family=Playfair+Display:wght@800&family=Abril+Fatface&display=swap">
<style>
  :root {
    --backdrop: #000000;
    --heading: #e8e8e8;
    --honey-light: #fcc93c;
    --honey-mid: #f7ad26;
    --honey-deep: #ee9216;
    --ink-brown: #4a2708;
    --ink-body: #3a2006;
    --badge-green: #5aa02c;
    --photo-sea: #5f8fae;
    --photo-cliff: #6f7d55;
    --photo-meadow: #6e9a4d;
    --white: #ffffff;
  }
  * { box-sizing: border-box; margin: 0; padding: 0; }
  html, body { width: 1200px; height: 507px; overflow: hidden; background: var(--backdrop); }
  .canvas { position: relative; width: 1200px; height: 507px; background: var(--backdrop); font-family: "Arimo", Arial, sans-serif; }

  .panel-heading { position: absolute; top: 46px; width: 160px; margin-left: -80px; text-align: center; color: var(--heading); font-size: 15px; }

  .label {
    position: absolute; left: 149px; top: 91px; width: 936px; height: 348px; overflow: hidden;
    background: radial-gradient(ellipse at 40% 50%, var(--honey-light) 0%, var(--honey-mid) 55%, var(--honey-deep) 100%);
  }
  .label > * { position: absolute; }

  .photo { border-radius: 50%; border: 3px solid var(--white); }
  .photo--coast { left: 14px; top: 28px; width: 218px; height: 156px; background: linear-gradient(160deg, var(--photo-sea) 0%, #8fb3c9 45%, var(--photo-cliff) 100%); }
  .photo--kids { left: 480px; top: 40px; width: 202px; height: 146px; background: linear-gradient(180deg, #8fb8d6 0%, #a9c9b7 40%, var(--photo-meadow) 100%); }

  .side-copy { color: var(--ink-body); font-style: italic; font-size: 13px; line-height: 1.2; }
  .side-copy--a { left: 14px; top: 194px; width: 222px; text-align: justify; }
  .side-copy--b { left: 476px; top: 206px; width: 206px; padding: 8px 0; border-top: 1.5px solid var(--ink-brown); border-bottom: 1.5px solid var(--ink-brown); }

  .divider { top: 0; width: 2px; height: 100%; background: var(--ink-brown); opacity: .55; }
  .divider--left { left: 254px; }
  .divider--right { left: 456px; }

  .front-seal { left: 245px; top: 0; width: 220px; height: 210px; }
  .front-badge { left: 420px; top: 150px; width: 26px; height: 26px; border-radius: 50%; background: var(--badge-green); border: 2px solid var(--white); }
  .front-title { left: 256px; width: 200px; text-align: center; color: var(--ink-brown); white-space: nowrap; }
  .front-title--sub { top: 210px; font-family: "Playfair Display", Georgia, serif; font-weight: 800; font-size: 18px; letter-spacing: 1px; }
  .front-title--main { top: 232px; font-family: "Abril Fatface", Georgia, serif; font-size: 50px; line-height: 1.1; }

  .nutrition { left: 739px; top: 17px; width: 187px; height: 180px; background: var(--white); border: 1px solid #222; padding: 4px 6px; color: #111; font-size: 7px; line-height: 1.35; }
  .nutrition h2 { font-size: 16px; font-weight: 700; line-height: 1; border-bottom: 5px solid #111; padding-bottom: 3px; margin-bottom: 2px; }
  .nutrition .row { display: flex; justify-content: space-between; border-bottom: 1px solid #555; }
  .nutrition .row--thick { border-bottom: 3px solid #111; }
  .nutrition .indent { padding-left: 8px; }
  .nutrition .bold { font-weight: 700; }

  .back-box { left: 734px; top: 221px; width: 192px; height: 101px; background: var(--white); }
</style>
</head>
<body>
<div class="canvas">
  <div class="panel-heading" style="left:266px">Side A</div>
  <div class="panel-heading" style="left:487px">Front</div>
  <div class="panel-heading" style="left:720px">Side B</div>
  <div class="panel-heading" style="left:960px">Back</div>

  <section class="label">
    <div class="photo photo--coast" role="img" aria-label="Photo of the rugged coastline with cliffs meeting the sea"></div>
    <p class="side-copy side-copy--a">Dellacourt Brothers Pine Cove Wild and Raw Honey is produced by thousands of hardworking honeybees in the remote coastal area of Big Sur, California. The bees are surrounded by Federal Woodland Trust land, so no pesticides come in contact with the bees or this honey.</p>

    <div class="divider divider--left"></div>
    <div class="divider divider--right"></div>

    <svg class="front-seal" viewBox="0 0 220 210">
      <defs>
        <path id="seal-arc" d="M 23.7 141.4 A 92 92 0 1 1 196.3 141.4"/>
        <linearGradient id="family-tone" x1="0" y1="0" x2="0" y2="1">
          <stop offset="0" stop-color="#c9c4ba"/>
          <stop offset="1" stop-color="#7d786f"/>
        </linearGradient>
      </defs>
      <text font-family="Playfair Display, Georgia, serif" font-weight="800" font-size="12.5" fill="#4a2708" letter-spacing="0.6">
        <textPath href="#seal-arc" startOffset="50%" text-anchor="middle">DELLACOURT BROTHERS PINE COVE</textPath>
      </text>
      <circle cx="110" cy="110" r="74" fill="url(#family-tone)" stroke="#ffffff" stroke-width="3" role="img" aria-label="Black and white photo of the three brothers with their dad"/>
    </svg>
    <div class="front-badge"></div>
    <div class="front-title front-title--sub">WILD AND RAW</div>
    <div class="front-title front-title--main">HONEY</div>

    <div class="photo photo--kids" role="img" aria-label="Photo of the brothers jumping in a sunny meadow"></div>
    <p class="side-copy side-copy--b">The honey is collected by Jasper (10), Ottis (7) and Rowan Dellacourt (5) with help from their Dad.</p>

    <div class="nutrition">
      <h2>Nutrition Facts</h2>
      <div>Serving Size 1 Tbsp (21g)</div>
      <div class="row row--thick">Servings Per Container 22</div>
      <div class="row bold">Amount Per Serving</div>
      <div class="row row--thick"><span class="bold">Calories 60</span></div>
      <div class="row" style="justify-content:flex-end">% Daily Value</div>
      <div class="row"><span><b>Total Fat</b> 0g</span><span>0%</span></div>
      <div class="row"><span><b>Sodium</b> 0mg</span><span>0%</span></div>
      <div class="row"><span><b>Total Carbohydrate</b> 17g</span><span>6%</span></div>
      <div class="row row--thick indent"><span>Sugars 16g</span></div>
    </div>
    <div class="back-box"></div>
  </section>
</div>
</body>
</html>
```